Beer Garden Specials socials

Hello - simular to last project but for a different venue.

Specials are:
$5 @ 5pm - $5 Pints Wednesday - Sunday.
Wednesday $1 Chicken Wings
Thursday - $12.50 Pizzas
Friday $12.48 Pint & Burger 12-3pm
Kids Eat Free - Saturdays & Sundays 12-3pm

Need an instagram image for each special and also a combined Facebook cover.
Needs to be classy but playful

```html
<!DOCTYPE html>
<html lang="en">
<head>
<meta charset="utf-8">
<title>Hopfield Yard Brewing – Special Promo</title>
<link href="https://fonts.googleapis.com/css2?family=Montserrat:wght@500;600;700;800;900&display=swap" rel="stylesheet">
<style>
  :root {
    --frame: #7b2800;
    --card: #f1bd56;
    --ink: #6a1e02;
    --box: #6a1e02;
    --box-glass: rgba(70, 30, 10, 0.55);
    --on-box: #ffffff;
    --food-light: #e9a64a;
    --food-mid: #c8742b;
    --food-dark: #8a3d12;
  }
  * { margin: 0; padding: 0; box-sizing: border-box; }
  html, body { width: 1100px; height: 1200px; overflow: hidden; }
  body {
    background: var(--frame);
    font-family: "Montserrat", sans-serif;
    color: var(--ink);
    position: relative;
  }
  .card {
    position: absolute;
    left: 80px; top: 119px;
    width: 939px; height: 939px;
    background: var(--card);
    box-shadow: 0 14px 16px -6px rgba(40, 10, 0, 0.55);
    overflow: hidden;
  }
  .abs { position: absolute; white-space: nowrap; }

  .headline-top {
    left: 52px; top: 34px;
    font-size: 66px; font-weight: 900; line-height: 1;
    letter-spacing: -1px;
  }
  .headline-main {
    left: 46px; top: 80px;
    font-size: 168px; font-weight: 900; line-height: 1;
    letter-spacing: -6px;
  }

  .brand {
    left: 727px; top: 50px; width: 180px;
    text-align: center;
    font-weight: 800; color: var(--ink);
  }
  .brand-dot {
    width: 36px; height: 36px; border-radius: 50%;
    background: var(--ink); margin: 0 auto 36px;
  }
  .brand-name { font-size: 29px; line-height: 1; letter-spacing: 1px; }
  .brand-sub { font-size: 21px; line-height: 1.2; letter-spacing: 5px; margin-top: 8px; }
  .brand-tag { font-size: 10px; letter-spacing: 3px; margin-top: 6px; }

  .connectors { left: 0; top: 0; width: 939px; height: 939px; }

  .food { left: 0; top: 410px; width: 630px; height: 529px; }

  .deal {
    background: var(--box);
    color: var(--on-box);
    text-align: center;
    display: flex; flex-direction: column; align-items: center; justify-content: center;
  }
  .deal-day { font-weight: 600; line-height: 1.1; }
  .deal-price { font-weight: 800; line-height: 1; letter-spacing: -1px; }
  .deal-item { font-weight: 600; line-height: 1.2; }

  .deal--pints { left: 329px; top: 274px; width: 164px; height: 120px; }
  .deal--pints .deal-day { font-size: 13.5px; }
  .deal--pints .deal-price { font-size: 56px; margin: 4px 0 6px; }
  .deal--pints .deal-item { font-size: 13.5px; }

  .deal--burger { left: 493px; top: 513px; width: 164px; height: 121px; }
  .deal--burger .deal-day { font-size: 25px; }
  .deal--burger .deal-price { font-size: 42px; margin: 2px 0 8px; }
  .deal--burger .deal-item { font-size: 12.5px; }

  .deal--wings { left: 704px; top: 672px; width: 155px; height: 142px; }
  .deal--wings .deal-day { font-size: 14.5px; }
  .deal--wings .deal-price { font-size: 64px; margin: 4px 0 8px; }
  .deal--wings .deal-item { font-size: 14px; }

  .deal--pizza {
    left: 67px; top: 683px; width: 194px; height: 119px;
    background: var(--box-glass);
  }
  .deal--pizza .deal-day { font-size: 32px; }
  .deal--pizza .deal-price { font-size: 46px; }
  .deal--pizza .deal-item { font-size: 16px; }

  .kids { left: 672px; top: 306px; width: 250px; text-align: center; }
  .kids-lead { font-size: 30px; font-weight: 600; letter-spacing: 10px; line-height: 1; margin-right: -10px; }
  .kids-free { font-size: 90px; font-weight: 800; line-height: 1; letter-spacing: -1px; margin-top: 10px; }
  .kids-days { font-size: 17.5px; font-weight: 700; line-height: 1; letter-spacing: -0.2px; margin-top: -4px; }
  .kids-time { font-size: 64px; font-weight: 800; line-height: 1; letter-spacing: -1px; margin-top: 14px; }
</style>
</head>
<body>
  <main class="card">
    <h1>
      <span class="abs headline-top">SPECIAL</span>
      <span class="abs headline-main">PROMO</span>
    </h1>

    <div class="abs brand" aria-label="Hopfield Yard Brewing">
      <div class="brand-dot"></div>
      <div class="brand-name">HOPFIELD</div>
      <div class="brand-sub">YARD</div>
      <div class="brand-tag">BREWING</div>
    </div>

    <svg class="abs connectors" viewBox="0 0 939 939" aria-hidden="true">
      <g fill="none" stroke="var(--ink)" stroke-width="2.2">
        <polyline points="329,326 119,326 119,406"/>
        <polyline points="191,431 347,431 347,447"/>
        <polyline points="347,447 575,447 575,513"/>
        <polyline points="704,738 533,738 533,806"/>
      </g>
    </svg>

    <svg class="abs food" viewBox="0 0 630 529" role="img" aria-label="Photo of a pint of beer, a grilled pineapple burger, a pizza and a plate of chicken wings">
      <defs>
        <radialGradient id="foodGlow" cx="45%" cy="55%" r="70%">
          <stop offset="0%" stop-color="var(--food-light)"/>
          <stop offset="60%" stop-color="var(--food-mid)"/>
          <stop offset="100%" stop-color="var(--food-dark)"/>
        </radialGradient>
      </defs>
      <path d="M0 6 Q90 -4 180 6 L182 60 Q290 20 440 70 Q500 200 520 330 Q610 350 630 420 L630 529 L0 529 Z" fill="url(#foodGlow)"/>
    </svg>

    <div class="abs deal deal--pints">
      <span class="deal-day">Wednesday - Sunday</span>
      <span class="deal-price">$5</span>
      <span class="deal-item">5pm Pints</span>
    </div>

    <div class="abs deal deal--burger">
      <span class="deal-day">Friday</span>
      <span class="deal-price">$12.48</span>
      <span class="deal-item">Pint &amp; Burger 12-3pm</span>
    </div>

    <div class="abs deal deal--wings">
      <span class="deal-day">Wednesday</span>
      <span class="deal-price">$1</span>
      <span class="deal-item">Chicken Wings</span>
    </div>

    <div class="abs deal deal--pizza">
      <span class="deal-day">Thursday</span>
      <span class="deal-price">$12.50</span>
      <span class="deal-item">Pizza</span>
    </div>

    <section class="abs kids">
      <div class="kids-lead">KIDS EAT</div>
      <div class="kids-free">FREE</div>
      <div class="kids-days">SATURDAYS &amp; SUNDAYS</div>
      <div class="kids-time">12-3PM</div>
    </section>
  </main>
</body>
</html>
```